Infographic to communicate Cyber Security and Insurance Product Offering for IT Service Providers

We need an inspirational infographic that shows how VaultBridge works with KRE (an MSP partner) to help organisations close the loop on cyber risk. The design should illustrate the layers of the IT infrastructure stack and the systems and processes that wrap around it to protect and mitigate against risk.
At the core: MSP Services (Desktop, Software, Website). Surrounding this: VaultBridge Governance & Protection, leading into an Incident layer that connects to VaultBridge Insurance and Incident Response, linked by a continuous feedback loop. The outer circle should represent the constant threat of cyber attack.
VaultBridge core offerings for this graphic:
Shield Attest (compliance/assurance product)
Shield Cover
KRE Primary Services (directly connected to VaultBridge):
Managed IT Services
Disaster Recovery as a Service (DRaaS)
E8 Security Packages
Cloud Hosting & Infrastructure
KRE Secondary Services (supporting but not directly anchored):
Telephony & Unified Communications
Networking Services
Data Backup & Storage Solutions
Professional Services & Consulting
Procurement & Licensing
Training & User Awareness
Style: Modern, professional, and client-friendly, with a technology-inspired colour palette.
Deliverables: Polished colour version plus editable source files — preferably in Figma, or alternatively if not possible using either Adobe Illustrator (.AI) or a layered Photoshop (.PSD) (e.g. industry standards for editable design).
Rewards: The winning design prize will be increased by $100, and we will also award $50 each to the 2nd and 3rd place runner-ups, as our way of giving a little more back.
A simple wireframe visual guide has been uploaded as a reference, but this should in no way limit or restrict your creativity. We encourage original, innovative approaches to bring this concept to life.
Ownership & Exclusivity: As per ArtFolio’s T&Cs, all rights to the winning design will transfer to us once the project is complete for our ongoing use. We also kindly ask that the work created here remain exclusive to this project, meaning it won’t be reused or lightly modified for other clients in the future. The reason is simple: once we’ve invested in and paid for a design, we want to be confident it won’t turn up on a competitor’s website with just a different colour scheme. Thanks again for respecting that. [Note:- The designs submitted so far haven’t quite hit the mark, so I’ve put together a couple of slides to clarify direction. These outline the key stakeholders, the current IT services and challenges, how the Brimlox product addresses those challenges, and a simple version of what we’d like the infographic to convey. Please review these slides carefully, as they should give you a clearer understanding of the story we want the design to tell.]
Target Market(s)
Small to Medium sized businesses
Colors
Designer to choose colors to be used in the design.
Look and feel

```html
<!DOCTYPE html>
<html lang="en">
<head>
<meta charset="utf-8">
<title>KRE &amp; VaultBridge – Closing the Loop on Cyber Risk</title>
<link rel="stylesheet" href="https://fonts.googleapis.com/css2?family=Montserrat:wght@500;600;700;800&display=swap">
<style>
  :root {
    --page-grey: #e8e8e8;
    --navy: #0f2743;
    --navy-deep: #0c1d30;
    --card: #0e1e2f;
    --green: #1fcb8e;
    --teal: #3fb7a3;
    --white: #ffffff;
    --text-soft: #eef4f7;
  }
  * { margin: 0; padding: 0; box-sizing: border-box; }
  html, body {
    width: 1200px; height: 785px; overflow: hidden;
    background: var(--page-grey);
    font-family: "Montserrat", Arial, sans-serif;
  }
  .canvas { position: relative; width: 1200px; height: 785px; }
  .board {
    position: absolute; left: 64px; top: 82px; width: 1072px; height: 603px;
    background:
      radial-gradient(circle at 100% 0%, rgba(120,170,80,0.75) 0, rgba(60,120,80,0.25) 90px, rgba(15,39,67,0) 190px),
      radial-gradient(circle at 0% 85%, rgba(40,110,120,0.35) 0, rgba(15,39,67,0) 180px),
      var(--navy);
    overflow: hidden;
  }
  .diagram { position: absolute; left: 0; top: 0; }

  .service-card {
    position: absolute; top: 215px; width: 207px; height: 337px;
    background: var(--card);
    border-radius: 14px;
    box-shadow: 0 0 24px rgba(0,0,0,0.35);
    overflow: hidden;
  }
  .service-card--primary { left: 117px; }
  .service-card--secondary { left: 876px; }
  .service-card__header {
    height: 56px;
    background: linear-gradient(90deg, var(--teal), var(--green));
    color: var(--white);
    text-align: center;
    display: flex; flex-direction: column; justify-content: center;
    font-weight: 800; line-height: 1.1;
  }
  .service-card__partner { font-size: 19px; letter-spacing: 0.3px; }
  .service-card__tier { font-size: 19px; font-weight: 700; }
  .service-list { list-style: none; padding: 20px 10px 0 43px; }
  .service-list li {
    position: relative;
    color: var(--text-soft);
    font-size: 14px; font-weight: 500; line-height: 18px;
    margin-bottom: 9px;
  }
  .service-list li::before {
    content: "→";
    position: absolute; left: -27px; top: 0;
    color: var(--green); font-weight: 600;
  }

  .core-title {
    position: absolute; left: 480px; width: 240px; top: 289px;
    text-align: center; color: var(--white);
    font-size: 25px; font-weight: 800; line-height: 29px; letter-spacing: 0.5px;
  }
  .layer-pill {
    position: absolute; left: 531px; width: 136px; height: 30px;
    border-radius: 15px;
    background: linear-gradient(90deg, #26c79b, var(--green));
    display: flex; align-items: center;
    color: var(--white); font-size: 14px; font-weight: 800; letter-spacing: 0.2px;
  }
  .layer-pill__icon {
    width: 22px; height: 22px; border-radius: 50%;
    background: var(--white); margin: 0 10px 0 5px;
    display: flex; align-items: center; justify-content: center;
  }
  .layer-pill--desktop { top: 362px; }
  .layer-pill--software { top: 397px; }
  .layer-pill--website { top: 433px; }

  .node-label {
    position: absolute; width: 80px; text-align: center;
    color: var(--white); font-size: 10.5px; font-weight: 800; top: 505px;
  }
  .node-label--incident { left: 431px; }
  .node-label--insurance { left: 691px; }
</style>
</head>
<body>
<div class="canvas">
  <div class="board"></div>

  <svg class="diagram" width="1200" height="785" viewBox="0 0 1200 785" aria-hidden="true">
    <defs>
      <radialGradient id="middle-ring-fill" cx="50%" cy="45%" r="55%">
        <stop offset="60%" stop-color="#2a4a66" stop-opacity="0.35"/>
        <stop offset="100%" stop-color="#3f6a86" stop-opacity="0.55"/>
      </radialGradient>
      <path id="threat-arc" d="M404,384 A196,196 0 0 1 796,384"/>
      <path id="governance-arc" d="M448,384 A152,152 0 0 1 752,384"/>
      <path id="protection-arc" d="M466,384 A134,134 0 0 1 734,384"/>
    </defs>

    <!-- feedback loop -->
    <g class="feedback-loop" fill="none" stroke="#1fcb8e" stroke-width="4.5" stroke-linecap="round" stroke-linejoin="round">
      <path d="M214,198 V165 A50,50 0 0 1 264,115 H942 A50,50 0 0 1 992,165 V204"/>
      <path d="M980,192 L992,204 L1004,192"/>
      <path d="M1008,571 V603 A50,50 0 0 1 958,653 H281 A50,50 0 0 1 231,603 V566"/>
      <path d="M219,578 L231,566 L243,578"/>
    </g>

    <!-- threat layer -->
    <circle cx="600" cy="384" r="245" fill="#ffffff" fill-opacity="0.03" stroke="#1fcb8e" stroke-opacity="0.45" stroke-width="1"/>
    <!-- governance layer -->
    <circle cx="600" cy="384" r="184" fill="url(#middle-ring-fill)" stroke="#1fcb8e" stroke-opacity="0.4" stroke-width="1"/>
    <!-- core -->
    <circle cx="600" cy="384" r="125" fill="#0d1f31" stroke="#1fcb8e" stroke-width="2.5"/>

    <text font-family="Montserrat, Arial, sans-serif" font-weight="800" font-size="34" fill="#1fcb8e" letter-spacing="2">
      <textPath href="#threat-arc" startOffset="50%" text-anchor="middle">CYBER ATTACT</textPath>
    </text>
    <text font-family="Montserrat, Arial, sans-serif" font-weight="700" font-size="15" fill="#ffffff" letter-spacing="1">
      <textPath href="#governance-arc" startOffset="50%" text-anchor="middle">VAULTBRIDGE GOVERNANCE</textPath>
    </text>
    <text font-family="Montserrat, Arial, sans-serif" font-weight="700" font-size="15" fill="#ffffff" letter-spacing="1">
      <textPath href="#protection-arc" startOffset="50%" text-anchor="middle">AND PROTECTION</textPath>
    </text>

    <!-- incident & insurance nodes -->
    <circle cx="471.5" cy="511" r="39" fill="#0d1f31" stroke="#1fcb8e" stroke-width="2.5"/>
    <circle cx="731" cy="511" r="39" fill="#0d1f31" stroke="#1fcb8e" stroke-width="2.5"/>
  </svg>

  <section class="service-card service-card--primary">
    <header class="service-card__header">
      <span class="service-card__partner">KRE</span>
      <span class="service-card__tier">Primary Service</span>
    </header>
    <ul class="service-list">
      <li>Managed IT Services</li>
      <li>Disaster Recovery<br>as a Service (DRaaS)</li>
      <li>E8 Security Packages</li>
      <li>Cloud Hosting<br>&amp; Infrastructure</li>
    </ul>
  </section>

  <section class="service-card service-card--secondary">
    <header class="service-card__header">
      <span class="service-card__partner">KRE</span>
      <span class="service-card__tier">Secondary Service</span>
    </header>
    <ul class="service-list">
      <li>Telephony &amp; Unified<br>Communications</li>
      <li>Networking Services</li>
      <li>Data Backup &amp;<br>Storage Solutions</li>
      <li>Professional<br>Services &amp; Consulting</li>
      <li>Procurement &amp;<br>Licensing</li>
      <li>Training &amp; User<br>Awareness</li>
    </ul>
  </section>

  <h1 class="core-title">MSP<br>SERVICES</h1>

  <div class="layer-pill layer-pill--desktop">
    <span class="layer-pill__icon">
      <svg width="14" height="14" viewBox="0 0 14 14" fill="none" stroke="#4a5a66" stroke-width="1.2"><rect x="1.5" y="2" width="11" height="7.5" rx="1"/><path d="M7 9.5V12M4.5 12h5"/></svg>
    </span>DEKSTOP
  </div>
  <div class="layer-pill layer-pill--software">
    <span class="layer-pill__icon">
      <svg width="14" height="14" viewBox="0 0 14 14" fill="none" stroke="#4a5a66" stroke-width="1.2"><circle cx="7" cy="7" r="2"/><circle cx="7" cy="7" r="4.5" stroke-dasharray="2 1.5"/></svg>
    </span>SOFTWARE
  </div>
  <div class="layer-pill layer-pill--website">
    <span class="layer-pill__icon">
      <svg width="14" height="14" viewBox="0 0 14 14" fill="none" stroke="#4a5a66" stroke-width="1.1"><circle cx="7" cy="7" r="5.5"/><ellipse cx="7" cy="7" rx="2.4" ry="5.5"/><path d="M1.5 7h11M2.5 4h9M2.5 10h9"/></svg>
    </span>WEBSITE
  </div>

  <div class="node-label node-label--incident">INCIDENT</div>
  <div class="node-label node-label--insurance">INSURANCE</div>
</div>
</body>
</html>
```